Revamp my web site design

Willowbrook Care Practitioners is a not for profit organisation focused on providing emotional support and counselling services to those with cancer or affected by cancer including those bereaved.

Our web site is intended to welcome suffers to engage with the services of its members and is also provided to encourage additional counsellors to join the organisation and then supports its members with access to materials and courses to extend their professional development.

We have a limited budget and seek to not only improve the attractiveness of the site but also improve the functionality and ease of maintenance. Especially site administrtaion should allow for uploading documents, adding new members, news and events easily.

Existing site is www.willowbrookcare.com.au

```html
<!DOCTYPE html>
<html lang="en">
<head>
<meta charset="utf-8">
<title>Willowbrook Care Practitioners</title>
<link rel="stylesheet" href="https://fonts.googleapis.com/css2?family=PT+Serif&family=Arimo:wght@400;700&family=PT+Sans+Narrow:wght@700&display=swap">
<style>
  :root {
    --page: #ffffff;
    --ink: #111111;
    --nav-ink: #444444;
    --band-dark: #0b0b0b;
    --band-mid: #262626;
    --band-muted: #bdbdbd;
    --button-face: #f4f4f4;
    --button-ink: #333333;
    --body-ink: #555555;
    --link: #2a6fd6;
    --rule-dark: #000000;
    --rule-light: #e3e3e3;
    --portrait-top: #6e6e6e;
    --portrait-base: #3a3a3a;
  }
  * { margin: 0; padding: 0; box-sizing: border-box; }
  html, body {
    width: 1200px; height: 717px; overflow: hidden;
    background: var(--page);
  }
  .site { position: relative; width: 1200px; height: 717px; }

  .brand {
    position: absolute; left: 230px; top: 44px;
    font-family: "PT Serif", Georgia, serif;
    font-size: 34px; color: var(--ink);
  }

  .main-nav {
    position: absolute; top: 129px; left: 0; width: 1200px; height: 20px;
    font-family: "Arimo", Arial, sans-serif; font-size: 15px; color: var(--nav-ink);
  }
  .main-nav a { position: absolute; color: inherit; text-decoration: none; }

  .hero {
    position: absolute; left: 0; top: 153px; width: 1200px; height: 278px;
    background: radial-gradient(ellipse at 60% 40%, var(--band-mid) 0%, var(--band-dark) 75%);
    overflow: hidden;
  }
  .hero-title {
    position: absolute; left: 204px; top: 46px;
    font-family: "PT Serif", Georgia, serif; font-weight: 400;
    font-size: 30px; color: #ffffff;
  }
  .hero-lead {
    position: absolute; left: 204px; top: 98px; width: 480px;
    font-family: "PT Serif", Georgia, serif;
    font-size: 16.5px; line-height: 20px; color: var(--band-muted);
  }
  .hero-note {
    position: absolute; left: 204px; top: 156px; width: 445px;
    font-family: "Arimo", Arial, sans-serif;
    font-size: 11.6px; line-height: 16.7px; color: var(--band-muted);
  }
  .hero-note a { color: #ffffff; text-decoration: underline; }
  .button {
    position: absolute; top: 224px; height: 23px;
    border-radius: 12px; background: var(--button-face);
    box-shadow: 0 1px 2px rgba(0,0,0,.6);
    font-family: "Arimo", Arial, sans-serif; font-weight: 700;
    font-size: 11.6px; line-height: 23px; text-align: center;
    color: var(--button-ink); letter-spacing: .3px;
  }
  .button-find { left: 204px; width: 146px; }
  .button-members { left: 364px; width: 96px; }
  .portrait {
    position: absolute; left: 726px; top: 58px; width: 270px; height: 220px;
  }
  .portrait-caption {
    position: absolute; left: 786px; top: 255px; width: 150px; text-align: center;
    font-family: "Arimo", Arial, sans-serif; font-size: 10.5px; color: #a5a5a5;
  }

  .featured { position: absolute; left: 204px; top: 449px; width: 489px; }
  .featured-title {
    font-family: "PT Serif", Georgia, serif; font-weight: 400;
    font-size: 21.5px; color: var(--ink);
    padding-bottom: 3px; border-bottom: 3px solid var(--rule-dark);
  }
  .featured-text {
    margin-top: 10px;
    font-family: "Arimo", Arial, sans-serif;
    font-size: 10.1px; line-height: 12.6px; color: var(--body-ink);
    padding-bottom: 16px; border-bottom: 3px solid var(--rule-light);
  }
  .featured-text a { color: var(--link); }

  .sidebar-promo {
    position: absolute; left: 767px; top: 542px; width: 200px; text-align: center;
    font-family: "PT Sans Narrow", "Arial Narrow", sans-serif; font-weight: 700;
    font-size: 24px; line-height: 30px; color: var(--ink);
  }
</style>
</head>
<body>
<div class="site">
  <header>
    <div class="brand">Willowbrook Care Practitioners</div>
    <nav class="main-nav">
      <a style="left:548px">Home</a>
      <a style="left:623px">About</a>
      <a style="left:687px">Services</a>
      <a style="left:771px">Recognition</a>
      <a style="left:877px">Contact</a>
      <a style="left:954px">Blog</a>
    </nav>
  </header>

  <section class="hero">
    <h1 class="hero-title">Hi, I am R.Hartley</h1>
    <p class="hero-lead">Compassionate counselling for anyone touched by cancer, including families and those who are bereaved.</p>
    <p class="hero-note">Our members are qualified counsellors and psychologists. Read about <a>our services</a> or learn how to join our network as a member using the buttons below.</p>
    <div class="button button-find">Find A Counsellor</div>
    <div class="button button-members">Members</div>
    <svg class="portrait" viewBox="0 0 270 220" role="img" aria-label="Portrait photo of the counsellor">
      <defs>
        <radialGradient id="portraitFill" cx="0.5" cy="0.75" r="0.7">
          <stop offset="0" stop-color="var(--portrait-top)" stop-opacity="0.9"/>
          <stop offset="0.6" stop-color="var(--portrait-base)" stop-opacity="0.6"/>
          <stop offset="1" stop-color="var(--portrait-base)" stop-opacity="0"/>
        </radialGradient>
      </defs>
      <rect x="0" y="0" width="270" height="220" fill="url(#portraitFill)"/>
    </svg>
    <div class="portrait-caption">Counselling with care</div>
  </section>

  <section class="featured">
    <h2 class="featured-title">Featured</h2>
    <p class="featured-text">Diagnosis of cancer is a devastating experience for most people. Many people can <a>get support</a> by talking to close family or friends. However, it can sometimes help to talk to someone from outside of that circle who has been trained to listen and help you explore your feelings. You may feel as if you are riding an emotional rollercoaster. Often talking of your distress to those close to you can be difficult and painful. When someone is diagnosed with cancer, they and their family can feel shocked, numb, directionless and afraid. They often feel they need to talk things through in confidence with someone who understands the emotional challenges of cancer. Talking to a counsellor or psychologist experienced in cancer issues can ease the sense of isolation you may feel and help you find ways to face the challenges ahead.</p>
  </section>

  <aside class="sidebar-promo">Join our network<br>today!</aside>
</div>
</body>
</html>
```